TCH Business cards

We are a medium sized property company based in London and require a logo, Business card which reflects a professional company and incorporates our catchy name.

Our statement is (Building for the future) we like colours such as royal blue, greens and light browns but will look at anything.

Contact Information for Business Card

Tidecrest Holdings Limited
Unit 4, 3-5 Parbrook Lane
London
SE21 7QX

Web: www.tidecrestholdings.example

Email: tidecrestltd@mailbox.example

Telephone: +44-208-555-0142
Fax: +44-208-555-0187

```html
<!DOCTYPE html>
<html lang="en">
<head>
<meta charset="utf-8">
<title>Tidecrest Holdings Limited – Business Card</title>
<link rel="stylesheet" href="https://fonts.googleapis.com/css2?family=Bree+Serif&display=swap">
<style>
  :root {
    --paper: #ffffff;
    --slate: #666666;
    --mist: #e4e4e4;
    --stone: #a4a4a4;
    --navy-top: #02030e;
    --navy-bottom: #0a1f8c;
    --brand-blue: #1d4fe6;
    --text-light: #ffffff;
  }
  * { margin: 0; padding: 0; box-sizing: border-box; }
  html, body {
    width: 1200px;
    height: 791px;
    overflow: hidden;
    background: var(--paper);
  }
  .card {
    position: relative;
    width: 1200px;
    height: 791px;
    overflow: hidden;
    background: var(--paper);
    font-family: "Bree Serif", Georgia, serif;
  }
  .skyline-area {
    position: absolute;
    left: 525px;
    top: 0;
    width: 675px;
    height: 381px;
    background: linear-gradient(100deg, var(--mist) 0%, var(--stone) 55%, var(--mist) 100%);
  }
  .card-bands {
    position: absolute;
    inset: 0;
    width: 1200px;
    height: 791px;
  }
  .brand-lockup {
    position: absolute;
    left: 72px;
    top: 150px;
    width: 390px;
    display: flex;
    align-items: center;
    gap: 18px;
    color: var(--brand-blue);
    font-weight: 400;
  }
  .brand-mark {
    flex: 0 0 auto;
    width: 62px;
    height: 62px;
    background: var(--brand-blue);
  }
  .brand-name {
    display: flex;
    flex-direction: column;
    line-height: 1;
  }
  .brand-name-main {
    font-size: 58px;
    letter-spacing: 1px;
  }
  .brand-name-sub {
    margin-top: 10px;
    font-size: 23px;
    letter-spacing: 3px;
  }
  .contact-block {
    position: absolute;
    left: 427px;
    top: 424px;
    color: var(--text-light);
  }
  .company-name {
    font-size: 42px;
    font-weight: 400;
    line-height: 1;
    margin-bottom: 20px;
    letter-spacing: 0.3px;
  }
  .contact-list { list-style: none; }
  .contact-item {
    display: flex;
    align-items: center;
    height: 38px;
    font-size: 23px;
    line-height: 1;
  }
  .contact-item:nth-child(2) { margin-top: 19px; }
  .contact-item:nth-child(3) { margin-top: 29px; }
  .contact-item:nth-child(4) { margin-top: 30px; }
  .contact-icon {
    flex: 0 0 auto;
    width: 40px;
    height: 38px;
    margin-right: 14px;
  }
</style>
</head>
<body>
<main class="card">
  <div class="skyline-area" role="img" aria-label="Grey city skyline of building silhouettes"></div>

  <svg class="card-bands" viewBox="0 0 1039 685" preserveAspectRatio="none" aria-hidden="true">
    <defs>
      <linearGradient id="navy-fade" x1="0" y1="0" x2="0" y2="1">
        <stop offset="0" stop-color="var(--navy-top)"/>
        <stop offset="1" stop-color="var(--navy-bottom)"/>
      </linearGradient>
    </defs>
    <polygon class="navy-band" points="0,440 333,342 333,685 0,685" fill="url(#navy-fade)"/>
    <polygon class="slate-band" points="333,342 1039,135 1039,685 333,685" fill="var(--slate)"/>
  </svg>

  <div class="brand-lockup">
    <span class="brand-mark"></span>
    <span class="brand-name">
      <span class="brand-name-main">TIDECREST</span>
      <span class="brand-name-sub">HOLDINGS LIMITED</span>
    </span>
  </div>

  <section class="contact-block">
    <h1 class="company-name">Tidecrest Holdings Limited</h1>
    <ul class="contact-list">
      <li class="contact-item">
        <svg class="contact-icon" viewBox="0 0 40 38" aria-hidden="true">
          <path d="M4 20 L20 6 L36 20 L32 20 L32 34 L24 34 L24 25 L16 25 L16 34 L8 34 L8 20 Z" fill="#fff"/>
        </svg>
        <span>Unit 4, 3-5 Parbrook Lane London SE21 7QX</span>
      </li>
      <li class="contact-item">
        <svg class="contact-icon" viewBox="0 0 40 38" aria-hidden="true">
          <circle cx="18" cy="19" r="16" fill="#fff"/>
          <path d="M8 12 C12 10 15 14 13 18 C11 22 15 24 17 27 C18 30 15 33 13 31 C9 27 6 20 8 12 Z M20 6 C24 8 23 11 26 12 C30 13 31 18 28 20 C25 22 22 19 21 16 C20 13 18 10 20 6 Z" fill="var(--slate)"/>
        </svg>
        <span>www.tidecrestholdings.example</span>
      </li>
      <li class="contact-item">
        <svg class="contact-icon" viewBox="0 0 40 38" aria-hidden="true">
          <rect x="2" y="9" width="36" height="22" fill="#fff"/>
          <path d="M3 10 L20 23 L37 10 M3 30 L15 19 M37 30 L25 19" stroke="var(--slate)" stroke-width="1.6" fill="none"/>
        </svg>
        <span>tidecrestltd@mailbox.example</span>
      </li>
      <li class="contact-item">
        <svg class="contact-icon" viewBox="0 0 40 38" aria-hidden="true">
          <circle cx="20" cy="19" r="17" fill="none" stroke="#fff" stroke-width="2.2"/>
          <path d="M13 10 L17 9 L19 15 L16 17 C17 20 19 23 22 25 L24 22 L30 24 L29 28 C21 29 12 20 13 10 Z" fill="#fff"/>
        </svg>
        <span>+44-208-555-0142 +44-208-555-0187</span>
      </li>
    </ul>
  </section>
</main>
</body>
</html>
```